Shoes, Handbags and Accessories

The main business of the company are shoes and then handbags, jewellery and scarves to accessorize.

The design I am looking for is a "shabby chic" design, cursive font, perhaps with a vintage country feel to it.

Target Market(s)

Age group are more for the 25+, but more so 35+ ladies.

Industry/Entity Type

Business

Contact Information for Business Card

Lace Lane Boutique & Accessories
Marlene Toohey - P.O. Box 482, Kulbari W.A. 6281
Ph: (08) 97314426 fax: (08) 97314427 Mobile: 0419273561
Email:lacelane@brindanet.com.au
Web: www.lacelaneboutique.com.au
Like us on Friendsphere (Friendsphere logo)

Requirements
Must have
• As already described. A "faded" picture background is also another feature I like, but I don't want to create a cluttered look about the business card.
Nice to have
• Classy, stylish and comfortable shoes.

```html
<!DOCTYPE html>
<html lang="en">
<head>
<meta charset="utf-8">
<title>Lace Lane Boutique – Business Card</title>
<link rel="stylesheet" href="https://fonts.googleapis.com/css2?family=Cinzel:wght@400;600;700&family=Pinyon+Script&display=swap">
<style>
  :root {
    --page: #ffffff;
    --ink: #5a4134;
    --muted: #ab988c;
    --paper: #eeeae3;
    --paper-light: #f4f1ec;
    --paper-stain: #e4ddd1;
    --paper-edge: #cfc7bb;
    --damask-light: #f8f2e8;
    --damask-mid: #efe3d0;
    --damask-deep: #e6d6bd;
  }
  * { box-sizing: border-box; margin: 0; padding: 0; }
  html, body {
    width: 1200px; height: 1000px; overflow: hidden;
    background: var(--page);
  }
  .card {
    position: absolute; left: 45px; top: 157px;
    width: 1110px; height: 685px;
    font-family: "Cinzel", "Times New Roman", serif;
    color: var(--ink);
    overflow: hidden;
  }
  .damask-panel {
    position: absolute; top: 0; height: 100%;
    background:
      radial-gradient(ellipse 60% 18% at 40% 12%, var(--damask-light), transparent 70%),
      radial-gradient(ellipse 70% 20% at 60% 38%, var(--damask-light), transparent 70%),
      radial-gradient(ellipse 60% 18% at 35% 64%, var(--damask-light), transparent 70%),
      radial-gradient(ellipse 70% 20% at 60% 90%, var(--damask-light), transparent 70%),
      linear-gradient(180deg, var(--damask-mid), var(--damask-deep) 50%, var(--damask-mid));
  }
  .damask-panel--left { left: 0; width: 180px; }
  .damask-panel--right { right: 0; width: 183px; }
  .paper {
    position: absolute; left: 177px; top: 0;
    width: 753px; height: 100%;
    background:
      radial-gradient(ellipse 40% 25% at 85% 40%, rgba(214,202,184,0.35), transparent 70%),
      radial-gradient(ellipse 35% 20% at 15% 75%, rgba(214,202,184,0.3), transparent 70%),
      radial-gradient(ellipse 50% 30% at 50% 20%, var(--paper-light), transparent 70%),
      linear-gradient(180deg, var(--paper-light) 0%, var(--paper) 55%, var(--paper-stain) 100%);
    border-left: 2px solid var(--paper-edge);
    border-right: 2px solid var(--paper-edge);
    box-shadow: -2px 0 4px rgba(150,130,110,0.25), 2px 0 4px rgba(150,130,110,0.25);
    text-align: center;
  }
  .line { position: absolute; left: 0; width: 100%; white-space: nowrap; }
  .brand-name {
    top: 44px; font-family: "Pinyon Script", "Brush Script MT", cursive;
    font-size: 84px; font-weight: 400; line-height: 1.2; color: var(--ink);
  }
  .brand-tagline {
    top: 157px; font-size: 36px; font-weight: 600; color: var(--muted);
  }
  .person-name {
    top: 275px; font-size: 42px; font-weight: 600; letter-spacing: 1px;
  }
  .address { top: 398px; font-size: 25px; }
  .phones { top: 435px; font-size: 26px; letter-spacing: 0.5px; }
  .phones .gap { display: inline-block; width: 24px; }
  .label { color: var(--muted); }
  .email { top: 481px; font-size: 22px; }
  .website { top: 538px; font-size: 30px; font-weight: 700; letter-spacing: 0.5px; }
  .social {
    top: 600px; font-size: 25px;
    display: flex; justify-content: center; align-items: center; gap: 14px;
  }
  .social-mark {
    width: 40px; height: 40px; border-radius: 4px;
    background: #b1a398;
  }
</style>
</head>
<body>
  <div class="card">
    <div class="damask-panel damask-panel--left" role="img" aria-label="Faded cream damask pattern"></div>
    <div class="damask-panel damask-panel--right" role="img" aria-label="Faded cream damask pattern"></div>

    <div class="paper">
      <p class="line brand-name">Lace Lane Boutique</p>
      <p class="line brand-tagline">&amp; Accessories</p>

      <p class="line person-name">Marlene Toohey</p>

      <p class="line address">P.O. Box 482, Kulbari W.A. 6281</p>
      <p class="line phones">
        <span class="label">P:</span> (08) 9731 4426<span class="gap"></span>
        <span class="label">F:</span> (08) 9731 4427<span class="gap"></span>
        <span class="label">M:</span> 0419 273 561
      </p>
      <p class="line email"><span class="label">E:</span> lacelane@brindanet.com.au</p>

      <p class="line website">www.lacelaneboutique.com.au</p>

      <div class="line social">
        <span class="social-mark"></span>
        <span>Like us on Friendsphere</span>
      </div>
    </div>
  </div>
</body>
</html>
```